Design nogle Visitkort for VT Holding ApS

Design af visitkort med logo. VT Holding ApS er et selskab der beskæftiger sig med asset management, investeringsrådgivning og forretningsudvikling

```html
<!DOCTYPE html>
<html lang="da">
<head>
<meta charset="utf-8">
<title>VT Holding ApS – Visitkort</title>
<link href="https://fonts.googleapis.com/css2?family=Marcellus&family=Open+Sans:wght@400;600&display=swap" rel="stylesheet">
<style>
  :root {
    --backdrop: #1c1d21;
    --navy-deep: #05081a;
    --navy: #1a2350;
    --sky: #6f95e6;
    --sky-light: #9cb8f2;
    --band: #3d5bbd;
    --pill-a: #4063cf;
    --pill-b: #5a80ea;
    --paper: #ffffff;
    --logo-light: #c9d6f5;
    --logo-dark: #3a55b0;
    --text-light: #ffffff;
    --rule: rgba(255,255,255,0.55);
  }
  * { margin: 0; padding: 0; box-sizing: border-box; }
  html, body { width: 1200px; height: 900px; overflow: hidden; }
  body {
    background: var(--backdrop);
    font-family: "Open Sans", Arial, sans-serif;
    position: relative;
  }
  .card {
    position: absolute;
    width: 660px;
    height: 380px;
    border-radius: 6px;
    overflow: hidden;
    box-shadow: 0 18px 40px rgba(0,0,0,0.5);
  }
  .card__shapes { position: absolute; inset: 0; }
  .card--front { left: 240px; top: 50px; }
  .card--back { left: 300px; top: 470px; background: var(--paper); }

  .wordmark {
    position: absolute;
    display: flex;
    align-items: center;
    gap: 16px;
    font-family: "Marcellus", Georgia, serif;
    font-size: 40px;
    letter-spacing: 1px;
    white-space: nowrap;
  }
  .wordmark__dot {
    width: 22px; height: 22px; border-radius: 50%;
    flex: none;
  }
  .card--front .wordmark { left: 130px; top: 70px; color: var(--logo-light); }
  .card--front .wordmark__dot { background: var(--sky); }
  .card--back .wordmark { left: 200px; top: 30px; color: var(--logo-dark); }
  .card--back .wordmark__dot { background: var(--logo-dark); }

  .holder { position: absolute; left: 40px; top: 138px; color: var(--text-light); }
  .holder__name {
    font-size: 22px; font-weight: 600; letter-spacing: 4px; text-transform: uppercase;
  }
  .holder__web { display: flex; align-items: center; gap: 8px; font-size: 14px; margin-top: 10px; }

  .divider {
    position: absolute; left: 300px; top: 140px; width: 1px; height: 110px;
    background: var(--rule);
  }
  .contact {
    position: absolute; left: 325px; top: 150px; list-style: none;
    color: var(--text-light); font-size: 14px; line-height: 1.25;
  }
  .contact li { display: flex; align-items: flex-start; gap: 10px; margin-bottom: 12px; }
  .contact svg, .holder__web svg { flex: none; margin-top: 2px; }
</style>
</head>
<body>

  <section class="card card--front" aria-label="Visitkort forside">
    <svg class="card__shapes" viewBox="0 0 660 380" preserveAspectRatio="none">
      <defs>
        <linearGradient id="frontNavy" x1="0" y1="0" x2="0.3" y2="1">
          <stop offset="0" stop-color="#1a2350"/>
          <stop offset="1" stop-color="#05081a"/>
        </linearGradient>
        <linearGradient id="frontSky" x1="0" y1="0" x2="1" y2="0">
          <stop offset="0" stop-color="#4f78dc"/>
          <stop offset="1" stop-color="#9cb8f2"/>
        </linearGradient>
      </defs>
      <rect width="660" height="380" fill="url(#frontNavy)"/>
      <path d="M0 280 Q330 250 660 205 L660 380 L0 380 Z" fill="#e8eefb"/>
      <path d="M0 288 Q330 260 660 216 L660 380 L0 380 Z" fill="url(#frontSky)"/>
    </svg>
    <div class="wordmark">
      <span class="wordmark__dot"></span>
      <span>VT Holding ApS</span>
    </div>
  </section>

  <section class="card card--back" aria-label="Visitkort bagside">
    <svg class="card__shapes" viewBox="0 0 660 380" preserveAspectRatio="none">
      <defs>
        <linearGradient id="pillBlue" x1="0" y1="0" x2="1" y2="1">
          <stop offset="0" stop-color="#4063cf"/>
          <stop offset="1" stop-color="#5a80ea"/>
        </linearGradient>
      </defs>
      <rect x="0" y="108" width="420" height="158" fill="#3d5bbd"/>
      <rect x="300" y="150" width="260" height="190" rx="95" fill="url(#pillBlue)"/>
      <rect x="300" y="150" width="120" height="116" fill="url(#pillBlue)"/>
    </svg>

    <div class="wordmark">
      <span class="wordmark__dot"></span>
      <span>VT Holding ApS</span>
    </div>

    <div class="holder">
      <p class="holder__name">Anna Berg</p>
      <p class="holder__web">
        <svg width="14" height="14" viewBox="0 0 14 14" fill="none" stroke="#fff" stroke-width="1.3"><circle cx="7" cy="7" r="6"/><path d="M1 7h12M7 1c2.5 3 2.5 9 0 12M7 1c-2.5 3-2.5 9 0 12"/></svg>
        www.vtholding-demo.dk
      </p>
    </div>

    <div class="divider"></div>

    <ul class="contact">
      <li>
        <svg width="14" height="16" viewBox="0 0 14 16"><path d="M7 0a5.5 5.5 0 0 0-5.5 5.5C1.5 10 7 16 7 16s5.5-6 5.5-10.5A5.5 5.5 0 0 0 7 0zm0 7.6a2.1 2.1 0 1 1 0-4.2 2.1 2.1 0 0 1 0 4.2z" fill="#fff"/></svg>
        <span>12 Fjordvej,<br>8000 Aarhus C</span>
      </li>
      <li>
        <svg width="14" height="14" viewBox="0 0 14 14"><path d="M3 1l2.5 3-1.3 1.6a8 8 0 0 0 4.2 4.2L10 8.5l3 2.5-1.5 2.3C6 13 1 8 .7 2.5z" fill="#fff"/></svg>
        <span>+45 8000 1122</span>
      </li>
      <li>
        <svg width="14" height="14" viewBox="0 0 14 14" fill="#fff"><rect x="3" y="0" width="8" height="4"/><rect x="0" y="5" width="14" height="6" rx="1"/><rect x="3" y="9" width="8" height="5" fill="#fff" stroke="#4063cf" stroke-width="1"/></svg>
        <span>+45 8000 1123</span>
      </li>
      <li>
        <svg width="16" height="12" viewBox="0 0 16 12" fill="none" stroke="#fff" stroke-width="1.3"><rect x=".7" y=".7" width="14.6" height="10.6"/><path d="M.7.7L8 7l7.3-6.3"/></svg>
        <span>anna.berg@vtholding-demo.dk</span>
      </li>
    </ul>
  </section>

</body>
</html>
```